Social Media Graphics - ALL TEXT RK

We are looking for a series of social media graphics for Instagram (standard size 1:1 (1080x1080px) that are ALL TEXT. We want the following quotes below on each graphic; one quote per graphic. AND, In very small letters at the bottom of each graphic, add @RKMarlowLive

The look and feel of these graphics should be complimentary to the color palette attached below; but keep them simple. But the design is up to you; at the end of this document, I provided various samples of all text graphics that I like as examples.

Target Market(s)

women looking to lose weight

Industry/Entity Type

health and wellness

Colors
E54698
E96AAD
F1A4CE
F9D9EA
FCEFF6

Requirements
Must have
• the quotes in the document
Should not have
• no stock photography

```html
<!DOCTYPE html>
<html lang="en">
<head>
<meta charset="utf-8">
<title>Quote Graphic – RK</title>
<link rel="stylesheet" href="https://fonts.googleapis.com/css2?family=Montserrat:wght@600;700;800&display=swap">
<style>
  :root {
    --pink-deep: #E54698;
    --pink-main: #E96AAD;
    --pink-mid: #F1A4CE;
    --pink-soft: #F9D9EA;
    --pink-pale: #FCEFF6;
    --white: #FFFFFF;
    --quote-text: #FBEAF3;
  }
  html, body {
    margin: 0;
    padding: 0;
    width: 1200px;
    height: 1200px;
    overflow: hidden;
    background: var(--pink-pale);
  }
  .quote-graphic {
    display: block;
    width: 1200px;
    height: 1200px;
  }
  .quote-copy {
    font-family: 'Montserrat', sans-serif;
    font-weight: 600;
    font-size: 47px;
    fill: var(--quote-text);
  }
  .quote-mark {
    font-family: 'Montserrat', sans-serif;
    font-weight: 800;
    font-size: 170px;
    fill: var(--quote-text);
  }
  .handle {
    font-family: 'Montserrat', sans-serif;
    font-weight: 700;
    font-size: 37px;
    fill: var(--pink-deep);
  }
</style>
</head>
<body>
<svg class="quote-graphic" viewBox="0 0 1080 1080" xmlns="http://www.w3.org/2000/svg" role="img" aria-label="Quote: You've been lied to – 'just eat less and exercise more' doesn't work in menpause. @RKMarlowLive">
  <defs>
    <linearGradient id="bg-wash" x1="0" y1="0" x2="1" y2="1">
      <stop offset="0" stop-color="var(--pink-mid)"/>
      <stop offset="0.35" stop-color="var(--pink-soft)"/>
      <stop offset="0.7" stop-color="var(--pink-pale)"/>
      <stop offset="1" stop-color="var(--pink-mid)"/>
    </linearGradient>
    <linearGradient id="card-fill" x1="0" y1="0" x2="1" y2="1">
      <stop offset="0" stop-color="#F6C3DE"/>
      <stop offset="0.28" stop-color="var(--pink-main)"/>
      <stop offset="0.5" stop-color="#E666A9"/>
      <stop offset="0.75" stop-color="var(--pink-main)"/>
      <stop offset="1" stop-color="#F7CDE3"/>
    </linearGradient>
  </defs>

  <!-- background -->
  <rect class="backdrop" x="0" y="0" width="1080" height="1080" fill="url(#bg-wash)"/>

  <!-- card shadow and card -->
  <rect class="card-shadow" x="162" y="133" width="803" height="803" fill="var(--pink-mid)" opacity="0.75"/>
  <rect class="card" x="148" y="118" width="802" height="802" fill="url(#card-fill)"/>

  <!-- diamond frame -->
  <g class="diamond-frame" transform="rotate(45 540 510)">
    <rect x="211" y="181" width="658" height="658" rx="42" fill="none" stroke="var(--pink-deep)" stroke-width="18"/>
    <rect x="211" y="181" width="658" height="658" rx="42" fill="none" stroke="var(--white)" stroke-width="8"/>
  </g>

  <!-- quote marks -->
  <text class="quote-mark quote-open" x="186" y="290">&#8220;</text>
  <text class="quote-mark quote-close" x="814" y="958">&#8221;</text>

  <!-- quote -->
  <text class="quote-copy" text-anchor="middle">
    <tspan x="530" y="397">You've been lied to -</tspan>
    <tspan x="515" y="465">'just eat less</tspan>
    <tspan x="540" y="532">and exercise more’</tspan>
    <tspan x="540" y="600">doesn't work in</tspan>
    <tspan x="540" y="667">menpause.</tspan>
  </text>

  <!-- handle -->
  <text class="handle" x="558" y="1046" text-anchor="middle">@RKMarlowLive</text>
</svg>
</body>
</html>
```